New bussiness card, using company logo.
Gerald Finch
Manager/Director
Finch Property Developments
Po Box 4637
Thuringowa Central
Qld
0412 558 306
gerald@finchpropertydevelopments
eye catching, vibrant colours, professional

It Company

```html
<!DOCTYPE html>
<html lang="en">
<head>
<meta charset="utf-8">
<title>Finch Property Developments — Business Cards</title>
<link rel="stylesheet" href="https://fonts.googleapis.com/css2?family=Open+Sans:wght@400;600;800&family=Exo+2:wght@500&display=swap">
<style>
  :root {
    --backdrop: #2b2630;
    --card-white: #ffffff;
    --brand-green: #6cb944;
    --brand-green-light: #8dc63f;
    --brand-red: #e0262d;
    --ink: #222222;
    --rule-grey: #cfcfcf;
    --text-font: "Open Sans", Arial, sans-serif;
    --web-font: "Exo 2", "Open Sans", sans-serif;
  }
  * { margin: 0; padding: 0; box-sizing: border-box; }
  html, body { width: 1200px; height: 767px; overflow: hidden; }
  body { background: var(--backdrop); font-family: var(--text-font); position: relative; }

  .card {
    position: absolute;
    width: 524px;
    height: 299px;
    border-radius: 22px;
    overflow: hidden;
    box-shadow: 0 6px 18px rgba(0,0,0,0.55);
  }
  .card--contact { left: 42px; top: 45px; background: var(--card-white); }
  .card--front-white { left: 608px; top: 48px; background: var(--card-white); }
  .card--front-green { left: 45px; top: 396px; background: linear-gradient(180deg, var(--brand-green), var(--brand-green-light)); }
  .card--front-red { left: 624px; top: 403px; background: var(--brand-red); }

  /* company name lockup */
  .brand {
    position: absolute;
    display: flex;
    align-items: center;
    gap: 12px;
    font-weight: 800;
    text-transform: uppercase;
    line-height: 1.05;
    letter-spacing: 0.5px;
  }
  .brand__mark { flex: none; }
  .brand__name { display: block; }

  .card--contact .brand { left: 24px; top: 82px; font-size: 19px; color: var(--brand-red); }
  .card--contact .brand__mark { width: 18px; height: 18px; background: var(--brand-green); }

  .card--front-white .brand,
  .card--front-green .brand,
  .card--front-red .brand {
    left: 0; right: 0; justify-content: center; top: 104px; font-size: 37px;
  }
  .card--front-white .brand { color: var(--brand-red); }
  .card--front-white .brand__mark { width: 30px; height: 30px; background: var(--brand-green); }
  .card--front-green .brand,
  .card--front-red .brand { color: var(--card-white); top: 112px; }
  .card--front-green .brand__mark,
  .card--front-red .brand__mark { width: 30px; height: 30px; border: 4px solid var(--card-white); }

  /* contact details */
  .divider { position: absolute; left: 263px; top: 54px; width: 1px; height: 118px; background: var(--rule-grey); }
  .contact { position: absolute; left: 273px; top: 60px; }
  .contact__name { font-size: 19px; font-weight: 600; color: var(--brand-green); line-height: 1.2; }
  .contact__role { font-size: 15px; color: var(--brand-red); line-height: 1.2; }
  .contact__line { display: flex; align-items: center; gap: 7px; color: var(--ink); }
  .contact__line--phone { margin-top: 16px; font-size: 14px; }
  .contact__line--email { margin-top: 12px; font-size: 11.5px; }
  .contact__line svg { flex: none; }

  .rule { position: absolute; left: 0; right: 0; height: 1px; background: var(--brand-red); }
  .rule--top { top: 228px; }
  .rule--bottom { top: 268px; }
  .address-band {
    position: absolute; left: 0; right: 0; top: 235px; height: 27px;
    background: var(--brand-green); color: var(--card-white);
    font-size: 14px; letter-spacing: 0.6px; text-align: center; line-height: 27px;
  }

  .website {
    position: absolute; left: 0; right: 0; text-align: center;
    font-family: var(--web-font); font-weight: 500; font-size: 13px; letter-spacing: 3.4px;
  }
  .card--front-white .website { top: 266px; color: var(--ink); }
  .website__accent { color: var(--brand-red); }
  .card--front-green .website,
  .card--front-red .website { top: 252px; color: var(--card-white); }
</style>
</head>
<body>

  <section class="card card--contact" aria-label="Business card, contact side">
    <div class="brand">
      <span class="brand__mark"></span>
      <span class="brand__name">Finch Property<br>Developments</span>
    </div>
    <div class="divider"></div>
    <div class="contact">
      <p class="contact__name">Gerald Finch</p>
      <p class="contact__role">Manager/Director</p>
      <p class="contact__line contact__line--phone">
        <svg width="10" height="12" viewBox="0 0 10 12" aria-hidden="true"><path d="M2 0.5 L4 3 L3 4.5 Q4 7.5 6 8.5 L7.5 7.5 L9.5 10 L8 11.5 Q2 10 0.5 2.5 Z" fill="#6cb944"/></svg>
        0412 558 306
      </p>
      <p class="contact__line contact__line--email">
        <svg width="11" height="8" viewBox="0 0 11 8" aria-hidden="true"><rect width="11" height="8" fill="#6cb944"/><path d="M0 0 L5.5 4.5 L11 0" stroke="#fff" stroke-width="1" fill="none"/></svg>
        gerald@finchpropertydevelopments.com
      </p>
    </div>
    <div class="rule rule--top"></div>
    <div class="address-band">Po Box 4637, Marrowdale Central , Tas</div>
    <div class="rule rule--bottom"></div>
  </section>

  <section class="card card--front-white" aria-label="Business card, white front">
    <div class="brand">
      <span class="brand__mark"></span>
      <span class="brand__name">Finch Property<br>Developments</span>
    </div>
    <p class="website">www.<span class="website__accent">finch</span>propertydevelopments.com</p>
  </section>

  <section class="card card--front-green" aria-label="Business card, green front">
    <div class="brand">
      <span class="brand__mark"></span>
      <span class="brand__name">Finch Property<br>Developments</span>
    </div>
    <p class="website">www.finchpropertydevelopments.com</p>
  </section>

  <section class="card card--front-red" aria-label="Business card, red front">
    <div class="brand">
      <span class="brand__mark"></span>
      <span class="brand__name">Finch Property<br>Developments</span>
    </div>
    <p class="website">www.finchpropertydevelopments.com</p>
  </section>

</body>
</html>
```